Lorna Tess Tresses Fancy Business Card’s

I want my business cards to be elite, original and very classy. I want the business cards to match the colors of my logo and to match the design posted. I would love the design of the picture I posted

I want the card all white .
The dripping on the top of the card I want it to match the pink color in my logo that’s also posted .
I need my logo on the business card !
I need my Instagram- @lorna.tess.tresses__
And my phone number - 582 907 3365

Target Market(s)

My target market is young woman age 23 to older woman to the age of 65
I want both older and younger women to love my design . I don’t want any cheap looking business cards

Industry/Entity Type

Hair And Beauty

Contact Information for Business Card

Add my logo
Add my Instagram- @lorna.tess.tresses__
My number - 582 907 3365
My website- www.lornatesstresses.example

Font styles to use
Serif
Script

Colors
ffffff
e667a6
e34298

Requirements
Must have
• The business cards must have my logo, my number , my website, and my Instagram!
Nice to have
• Nice to have glitter words that match my logo
• The business cards must look classy and mature
• I want them to be very unique!!
Should not have
• Should not have any colors that doesn’t match my logo ! This is very important! Please

```html
<!DOCTYPE html>
<html lang="en">
<head>
<meta charset="utf-8">
<title>Lorna Tess Tresses — Business Cards</title>
<link rel="stylesheet" href="https://fonts.googleapis.com/css2?family=Great+Vibes&family=Montserrat:wght@400;500&display=swap">
<style>
  :root {
    --backdrop: #e9e9eb;
    --card: #ffffff;
    --pink: #c8409a;
    --ink: #4a4a4c;
    --rule: #5a5a5c;
  }
  * { box-sizing: border-box; margin: 0; padding: 0; }
  html, body {
    width: 1200px; height: 985px; overflow: hidden;
    background: var(--backdrop);
  }
  .canvas { position: relative; width: 1200px; height: 985px; }
  .card {
    position: absolute; left: 220px; width: 760px; height: 430px;
    background: var(--card);
    box-shadow: 0 6px 18px rgba(0,0,0,.12);
  }
  .card--front { top: 45px; }
  .card--back { top: 510px; }

  .wordmark {
    font-family: "Montserrat", sans-serif;
    font-weight: 400;
    color: var(--pink);
    text-align: center;
    text-transform: uppercase;
    line-height: 1.2;
    letter-spacing: 0.16em;
  }
  .card--front .wordmark {
    position: absolute; left: 0; right: 0; top: 145px;
    font-size: 52px;
  }
  .card--back .wordmark {
    position: absolute; left: 30px; top: 165px; width: 300px;
    font-size: 32px;
  }
  .divider {
    position: absolute; left: 350px; top: 120px; width: 2px; height: 190px;
    background: var(--rule);
  }
  .contact {
    position: absolute; left: 385px; top: 112px;
    font-family: "Montserrat", sans-serif; color: var(--ink);
  }
  .contact__name {
    font-family: "Great Vibes", cursive; color: var(--pink);
    font-size: 50px; line-height: 1;
  }
  .contact__role { font-size: 19px; margin: 2px 0 22px; }
  .contact__list { list-style: none; font-size: 20px; }
  .contact__item {
    display: flex; align-items: center; gap: 10px; margin-bottom: 8px;
  }
  .contact__icon { width: 18px; height: 18px; flex: none; }
  .contact__accent { color: var(--pink); }
</style>
</head>
<body>
<main class="canvas">
  <section class="card card--front" aria-label="Card front">
    <p class="wordmark">Lorna Tess<br>Tresses</p>
  </section>

  <section class="card card--back" aria-label="Card back">
    <p class="wordmark">Lorna Tess<br>Tresses</p>
    <div class="divider"></div>
    <div class="contact">
      <p class="contact__name">Marissa Vale</p>
      <p class="contact__role">Manager</p>
      <ul class="contact__list">
        <li class="contact__item">
          <svg class="contact__icon" viewBox="0 0 24 24" aria-hidden="true"><path fill="#c8409a" d="M6.6 10.8a15 15 0 0 0 6.6 6.6l2.2-2.2c.3-.3.7-.4 1-.2 1.1.4 2.3.6 3.6.6.6 0 1 .4 1 1V20c0 .6-.4 1-1 1A17 17 0 0 1 3 4c0-.6.4-1 1-1h3.5c.6 0 1 .4 1 1 0 1.3.2 2.5.6 3.6.1.3 0 .7-.2 1z"/></svg>
          <span>582 907 3365</span>
        </li>
        <li class="contact__item">
          <svg class="contact__icon" viewBox="0 0 24 24" aria-hidden="true"><rect x="3" y="3" width="18" height="18" rx="4" fill="#c8409a"/></svg>
          <span>@lorna.tess.tresses__</span>
        </li>
        <li class="contact__item">
          <svg class="contact__icon" viewBox="0 0 24 24" aria-hidden="true"><circle cx="12" cy="12" r="9" fill="none" stroke="#c8409a" stroke-width="2.5"/><path d="M3 12h18M12 3c3 3 3 15 0 18M12 3c-3 3-3 15 0 18" fill="none" stroke="#c8409a" stroke-width="1.8"/></svg>
          <span>www.<span class="contact__accent">lornatesstresses</span>.example</span>
        </li>
      </ul>
    </div>
  </section>
</main>
</body>
</html>
```